Elementary School Profile of a Falconet

Please recreate a poster of our Profile of a Falconet traits that we desire to have when they graduate from 4th grade. This should be kid-friendly and kid-themed with icons to help communicate the Competencies. See attached six competencies and the "I can" statements next to. Our colors are navy, red and white. Our logo is attached as well. This will be made into a poster and displayed in each classroom, the office, and also used on social media.

```html
<!DOCTYPE html>
<html lang="en">
<head>
<meta charset="utf-8">
<title>Cedar Harbor Public Schools: Profile of a Falconet</title>
<link href="https://fonts.googleapis.com/css2?family=Luckiest+Guy&family=Fredoka:wght@600;700&family=Baloo+2:wght@600;700&family=Caveat:wght@600&display=swap" rel="stylesheet">
<style>
  :root {
    --stage: #1062b0;
    --paper: #efefee;
    --navy: #2d4e8a;
    --red: #e5485a;
    --sun: #ffc300;
    --sky: #10cdfb;
    --bullet: #1bb0d6;
    --communicator: #1080f0;
    --thinker: #fdc300;
    --responsible: #1fbdbd;
    --adaptable: #ef5f6b;
    --collaborator: #ff6a35;
    --compassion: #ff9af0;
  }
  * { box-sizing: border-box; margin: 0; padding: 0; }
  html, body { width: 1200px; height: 1200px; overflow: hidden; background: var(--stage); }
  .poster {
    position: absolute; left: 190px; top: 20px; width: 820px; height: 1160px;
    background: var(--paper); overflow: hidden;
    background-image: repeating-linear-gradient(to bottom, transparent 0 27px, rgba(45,78,138,.06) 27px 28px);
  }
  .sun-band { position: absolute; left: 0; top: 0; width: 820px; height: 250px; }
  .deco { position: absolute; }
  .header {
    position: absolute; left: 90px; top: 44px; width: 632px; height: 174px;
    background: #fff; transform: rotate(-0.6deg);
    box-shadow: 8px 8px 0 var(--navy);
    background-image: repeating-linear-gradient(to bottom, transparent 0 21px, #d7e3f2 21px 22px);
    overflow: hidden;
  }
  .header .holes { position: absolute; left: 12px; top: 48px; width: 8px; }
  .header .holes span { display: block; width: 7px; height: 7px; border-radius: 50%; background: var(--bullet); margin-bottom: 26px; }
  .brand { position: absolute; left: 30px; top: 36px; width: 160px; text-align: center; }
  .brand .mark { width: 70px; height: 70px; border-radius: 50%; background: var(--navy); margin: 0 auto 8px; }
  .brand .name { font-family: 'Fredoka', sans-serif; font-weight: 700; font-size: 20px; color: var(--red); white-space: nowrap; }
  .title {
    position: absolute; left: 200px; top: 32px; width: 420px;
    font-family: 'Luckiest Guy', sans-serif; font-weight: 400; color: var(--navy);
    font-size: 25px; line-height: 34px; letter-spacing: .3px; white-space: nowrap;
  }
  .title .sub {
    display: inline-block; margin-top: 4px; font-family: 'Caveat', cursive; font-weight: 600;
    color: var(--red); font-size: 31px; line-height: 38px; letter-spacing: 0;
    border-bottom: 3px solid var(--red);
  }
  .trait { position: absolute; left: 0; width: 820px; height: 130px; }
  .trait .badge {
    position: absolute; left: 51px; top: 4px; width: 124px; height: 124px; border-radius: 50%;
    display: flex; align-items: center; justify-content: center;
    box-shadow: 4px 4px 0 #fff; z-index: 3;
  }
  .trait .card {
    position: absolute; left: 160px; top: 30px; width: 592px; height: 96px;
    background: #fff; box-shadow: 8px 6px 0 var(--c); z-index: 0;
  }
  .trait .tab {
    position: absolute; left: 180px; top: 0; height: 42px; padding: 0 18px;
    background: var(--tabc, var(--c)); color: #fff; white-space: nowrap;
    font-family: 'Fredoka', sans-serif; font-weight: 700; font-size: 30px; line-height: 42px;
    box-shadow: 5px 4px 0 var(--navy); z-index: 2;
    text-shadow: 1px 1px 0 var(--navy), -1px -1px 0 var(--navy), 1px -1px 0 var(--navy), -1px 1px 0 var(--navy);
  }
  .trait ul {
    position: absolute; left: 190px; top: 58px; width: 560px; list-style: none; z-index: 1;
    font-family: 'Baloo 2', sans-serif; font-weight: 700; font-size: 13.4px; line-height: 20px; color: var(--navy);
    white-space: nowrap;
  }
  .trait li::before { content: "•"; color: var(--bullet); margin-right: 8px; }
  .communicator { top: 244px; --c: var(--communicator); }
  .thinker { top: 385px; --c: var(--thinker); }
  .responsible { top: 531px; --c: var(--responsible); }
  .adaptable { top: 671px; --c: var(--adaptable); }
  .collaborator { top: 812px; --c: var(--collaborator); }
  .compassionate { top: 949px; --c: var(--compassion); --tabc: var(--communicator); }
  .web {
    position: absolute; left: 245px; top: 1074px; width: 316px; height: 52px;
    background: var(--sun); box-shadow: 6px 6px 0 var(--navy);
    font-family: 'Fredoka', sans-serif; font-weight: 700; font-size: 22px; color: var(--navy);
    display: flex; align-items: center; justify-content: center; white-space: nowrap;
  }
</style>
</head>
<body>
<main class="poster">
  <svg class="sun-band" viewBox="0 0 820 250" aria-hidden="true">
    <path d="M150 0 H820 V150 Q760 110 700 150 L690 20 L160 70 Z" fill="var(--sun)"/>
    <path d="M0 130 Q40 120 90 180 Q60 220 0 200 Z" fill="var(--sun)"/>
  </svg>
  <div class="deco" role="img" aria-label="Open book illustration" style="left:0;top:0;width:150px;height:90px;background:#eee1c9;border-bottom:6px solid var(--navy);"></div>
  <div class="deco" role="img" aria-label="Pencil illustration" style="left:760px;top:140px;width:60px;height:70px;background:linear-gradient(135deg,#f6c04a,#fde29a);"></div>
  <div class="deco" role="img" aria-label="Pink ruler illustration" style="left:792px;top:450px;width:28px;height:180px;background:#f2849e;"></div>
  <div class="deco" role="img" aria-label="Crayon illustration" style="left:0;top:190px;width:40px;height:70px;background:linear-gradient(#f2ead8,#4b5fa8);"></div>
  <div class="deco" role="img" aria-label="Teal ruler illustration" style="left:0;top:860px;width:50px;height:130px;background:#6ccfd2;"></div>
  <div class="deco" role="img" aria-label="Eraser illustration" style="left:780px;top:880px;width:40px;height:70px;background:linear-gradient(#f2ead8,#4b5fa8);"></div>
  <svg class="deco" style="left:0;top:940px" width="820" height="220" viewBox="0 0 820 220" aria-hidden="true">
    <path d="M0 40 Q60 10 120 40 Q200 -10 280 40 Q420 20 560 30 Q620 -10 700 30 Q770 10 820 40 V220 H0 Z" fill="#fff"/>
    <path d="M0 165 Q90 135 170 160 Q260 185 360 150 Q460 120 560 150 Q680 180 820 150 V220 H0 Z" fill="var(--sky)"/>
  </svg>
  <div class="deco" role="img" aria-label="Pencil illustration" style="left:0;top:1085px;width:80px;height:75px;background:linear-gradient(135deg,#f6c04a,#fde29a);"></div>

  <header class="header">
    <div class="holes"><span></span><span></span><span></span></div>
    <div class="brand"><div class="mark"></div><div class="name">Cedar Harbor</div></div>
    <h1 class="title">Cedar Harbor Public Schools:<br>Profile of a Falconet<br><span class="sub">Early Learners and Elementary School</span></h1>
  </header>

  <section class="trait communicator">
    <div class="badge" style="background:var(--communicator)">
      <svg width="74" height="66" viewBox="0 0 74 66" aria-label="Speech bubble icon" role="img"><path d="M8 6 H66 Q70 6 70 10 V40 Q70 44 66 44 H56 L60 60 L42 44 H8 Q4 44 4 40 V10 Q4 6 8 6 Z" fill="#fff" transform="rotate(-6 37 33)"/></svg>
    </div>
    <div class="card"></div>
    <h2 class="tab">Communicator</h2>
    <ul>
      <li>I can use words, writing, and pictures to clearly share ideas.</li>
      <li>I can look at the speaker and listen carefully to understand what they are saying.</li>
      <li>I know how to adjust my communication for different places and people.</li>
    </ul>
  </section>

  <section class="trait thinker">
    <div class="badge" style="background:var(--thinker)">
      <svg width="72" height="72" viewBox="0 0 72 72" role="img" aria-label="Light bulb icon">
        <circle cx="36" cy="32" r="26" fill="#fff" stroke="var(--navy)" stroke-width="3"/>
        <path d="M36 14 a13 13 0 0 0 -8 23 v5 h16 v-5 a13 13 0 0 0 -8 -23 z" fill="var(--sun)" stroke="var(--navy)" stroke-width="3" stroke-linejoin="round"/>
        <path d="M29 47 h14 M31 52 h10" stroke="var(--navy)" stroke-width="3" stroke-linecap="round"/>
        <path d="M32 30 l4 5 l4 -5 M36 35 v7" fill="none" stroke="var(--navy)" stroke-width="2.5" stroke-linecap="round"/>
      </svg>
    </div>
    <div class="card"></div>
    <h2 class="tab">Critical Thinker</h2>
    <ul>
      <li>I can ask questions like "why" and "how" to learn more about the world.</li>
      <li>When faced with a problem, I can be creative and come up with different solutions.</li>
      <li>I can use facts and clues to help make wise decisions.</li>
    </ul>
  </section>

  <section class="trait responsible">
    <div class="badge" style="background:var(--responsible)">
      <svg width="70" height="84" viewBox="0 0 70 84" role="img" aria-label="Clipboard with check icon"><g transform="rotate(-6 35 42)"><rect x="8" y="8" width="46" height="66" rx="6" fill="#fff"/><rect x="20" y="3" width="22" height="8" rx="3" fill="var(--navy)"/></g><circle cx="52" cy="68" r="12" fill="#fff" stroke="var(--navy)" stroke-width="3"/><path d="M46 68 L51 73 L58 63" fill="none" stroke="#5cbf3a" stroke-width="4" stroke-linecap="round"/></svg>
    </div>
    <div class="card"></div>
    <h2 class="tab">Responsible</h2>
    <ul>
      <li>I can take ownership of my actions and remember to complete my job.</li>
      <li>I can take care of my belongings and always try my best in schoolwork.</li>
      <li>I can tell the truth and act with integrity even when no one is watching.</li>
    </ul>
  </section>

  <section class="trait adaptable">
    <div class="badge" style="background:var(--adaptable)">
      <svg width="72" height="72" viewBox="0 0 72 72" role="img" aria-label="Change arrows icon">
        <path d="M16 30 a21 21 0 0 1 38 -8" fill="none" stroke="#fff" stroke-width="6" stroke-linecap="round"/>
        <path d="M58 12 v14 h-14" fill="none" stroke="#fff" stroke-width="6" stroke-linecap="round" stroke-linejoin="round"/>
        <path d="M56 42 a21 21 0 0 1 -38 8" fill="none" stroke="#fff" stroke-width="6" stroke-linecap="round"/>
        <path d="M14 60 v-14 h14" fill="none" stroke="#fff" stroke-width="6" stroke-linecap="round" stroke-linejoin="round"/>
      </svg>
    </div>
    <div class="card"></div>
    <h2 class="tab">Adaptable</h2>
    <ul>
      <li>When a plan changes or a task is hard, I can stay calm and try a new way.</li>
      <li>I can learn from mistakes and use past knowledge to try new things.</li>
      <li>I can work and play well with people who are different from me.</li>
    </ul>
  </section>

  <section class="trait collaborator">
    <div class="badge" style="background:var(--collaborator)">
      <svg width="80" height="64" viewBox="0 0 80 64" role="img" aria-label="Handshake icon">
        <path d="M4 18 l12 -8 l10 16 l-12 8 z M76 18 l-12 -8 l-10 16 l12 8 z" fill="#fff" stroke="var(--navy)" stroke-width="2.5" stroke-linejoin="round"/>
        <path d="M22 22 l14 -6 h10 l12 6 l-6 12 l-14 -8 l-6 4 q-4 2 -6 -2 z" fill="#fff" stroke="var(--navy)" stroke-width="2.5" stroke-linejoin="round"/>
        <path d="M18 32 l16 16 q4 4 8 0 l4 -4 l6 -6 l-10 -10" fill="#fff" stroke="var(--navy)" stroke-width="2.5" stroke-linejoin="round"/>
        <path d="M26 40 l4 -4 M32 46 l4 -4 M38 50 l4 -4" stroke="var(--navy)" stroke-width="2.5" stroke-linecap="round"/>
      </svg>
    </div>
    <div class="card"></div>
    <h2 class="tab">Collaborator</h2>
    <ul>
      <li>I can share ideas and work together with a group to reach a common goal.</li>
      <li>I can listen to my teammates and respect their different ideas.</li>
      <li>I can know when to share, when to help others, and when to be the leader.</li>
    </ul>
  </section>

  <section class="trait compassionate">
    <div class="badge" style="background:var(--compassion)">
      <svg width="80" height="72" viewBox="0 0 80 72" role="img" aria-label="Heart in open hand icon">
        <path d="M40 40 C20 26 22 8 32 8 C36 8 39 11 40 14 C41 11 44 8 48 8 C58 8 60 26 40 40 Z" fill="#f0156a" stroke="var(--navy)" stroke-width="2.5" stroke-linejoin="round"/>
        <path d="M6 50 q10 -6 20 0 h16 q5 0 5 4 q0 4 -5 4 h-12 M47 55 l16 -8 q6 -2 7 3 l-20 14 q-4 2 -8 2 h-18 l-12 4" fill="#fff" stroke="var(--navy)" stroke-width="2.5" stroke-linecap="round" stroke-linejoin="round"/>
      </svg>
    </div>
    <div class="card"></div>
    <h2 class="tab">Compassionate</h2>
    <ul>
      <li>I can be empathetic, noticing how others are feeling (happy, sad, frustrated).</li>
      <li>I can use kind words and gentle actions to support their friends.</li>
      <li>I can look for ways to help their school and the community.</li>
    </ul>
  </section>

  <div class="web">cedarharbor.k12.example.org</div>
</main>
</body>
</html>
```